Economics of an Assumption vs Obtaining a New Loan at Current Market Rate

I need to marketing flyer that has fields that calculate mortgage payments amongst other calculations. I have a rough draft that I will attach.

The idea is to provide a tool for a real estate agent to use to illustrate to a potential buyer what a payment would be if they assumed the existing loan on the house or took out a new loan at current market.

The flyer needs to be able to allow an agent to drop in their logo, photo, and contact along with the loan officers photo and contact info.

You can google open house flyer to see examples of what the overall artwork and presentation can look like.

Target Market(s)

Home Buyers

Industry/Entity Type

Real Estate

Colors
F0912C
F2A743
F7CA91
FBE8D2
FDF5EE
EE7325
F08F49
F5BC92
FAE3D3
FDF4ED

Requirements
Must have
• A way to calculate mortgage payment
Nice to have
• Photo and logo drop ins

```html
<!DOCTYPE html>
<html lang="en">
<head>
<meta charset="utf-8">
<title>Nestora – Purchase Price Flyer</title>
<link rel="stylesheet" href="https://fonts.googleapis.com/css2?family=Poppins:wght@400;500;600;700;800&display=swap">
<style>
  :root {
    --orange: #ee7325;
    --orange-bright: #f07a10;
    --ink: #262626;
    --dark: #2a2a2a;
    --paper: #ffffff;
    --mist: #eceef3;
    --stage: #f1f1f1;
  }
  * { box-sizing: border-box; margin: 0; padding: 0; }
  html, body { width: 1200px; height: 2532px; overflow: hidden; }
  body { background: var(--stage); font-family: "Poppins", sans-serif; color: var(--ink); position: relative; }

  .flyer {
    position: absolute; left: 50px; top: 488px; width: 1100px; height: 1555px;
    background: var(--paper); overflow: hidden;
    box-shadow: 0 20px 50px rgba(0,0,0,.18);
  }
  .abs { position: absolute; }

  .brand { left: 63px; top: 80px; display: flex; align-items: center; gap: 18px; }
  .brand-dot { width: 26px; height: 26px; border-radius: 50%; background: var(--orange); }
  .brand-name { font-size: 84px; font-weight: 500; color: var(--ink); line-height: 1; letter-spacing: 1px; }

  .headline { left: 60px; top: 240px; font-size: 76px; font-weight: 800; line-height: 1.0; color: var(--ink); }

  .hero { left: 0; top: 0; width: 1100px; height: 470px; }

  .col-title { top: 486px; font-size: 34px; font-weight: 700; white-space: nowrap; }
  .col-title .pct { font-size: 36px; }
  .col-title .small { display: inline-block; font-size: 14px; line-height: 1; vertical-align: 4px; margin-left: 4px; }

  .row { height: 29px; display: flex; align-items: center; }
  .label { font-size: 19px; font-weight: 600; white-space: nowrap; }
  .field {
    position: absolute; height: 29px; background: var(--orange); color: #fff;
    font-size: 19px; font-weight: 400; display: flex; align-items: center; justify-content: center;
    white-space: nowrap;
  }
  .field.sm { font-size: 16px; }

  .diff-bar { left: 63px; top: 876px; width: 972px; height: 59px; display: flex; }
  .diff-left { width: 416px; border: 3px solid var(--orange); border-right: none; font-size: 33px; font-weight: 700; display: flex; align-items: center; justify-content: center; }
  .diff-right { flex: 1; background: var(--dark); color: #fff; font-size: 33px; font-weight: 700; display: flex; align-items: center; justify-content: center; }

  .tagline { left: 0; width: 1100px; top: 955px; text-align: center; font-size: 32px; font-weight: 700; }
  .tagline em { font-style: normal; color: var(--orange); }

  .panels { left: 0; top: 0; width: 1100px; height: 1555px; }

  .contact { width: 235px; top: 1084px; text-align: center; color: #fff; }
  .contact-title { font-size: 19px; font-weight: 700; color: var(--orange); height: 34px; }
  .contact.alt .contact-title { color: #fff; }
  .contact-icon { width: 54px; height: 54px; margin: 4px auto 0; display: block; }
  .contact-text { font-size: 19px; font-weight: 600; margin: 6px 0 18px; }

  .panel-brand { left: 801px; width: 235px; top: 1247px; display: flex; align-items: center; justify-content: center; gap: 10px; }
  .panel-brand .brand-dot { width: 14px; height: 14px; }
  .panel-brand .brand-name { font-size: 48px; color: #fff; }
</style>
</head>
<body>
<main class="flyer">

  <!-- hero photo with chevron edge -->
  <svg class="abs hero" viewBox="0 0 1100 470" aria-hidden="false">
    <defs>
      <linearGradient id="homeTone" x1="0" y1="0" x2="0" y2="1">
        <stop offset="0" stop-color="#8f9bbd"/>
        <stop offset=".35" stop-color="#b7b3be"/>
        <stop offset=".55" stop-color="#9a7a58"/>
        <stop offset=".85" stop-color="#7d6248"/>
        <stop offset="1" stop-color="#b8ab9c"/>
      </linearGradient>
    </defs>
    <polygon points="558,0 578,0 488,232 586,460 566,460 468,232" fill="var(--orange)"/>
    <polygon points="578,0 602,0 512,232 606,460 586,460 488,232" fill="var(--ink)"/>
    <polygon points="602,0 1100,0 1100,460 606,460 512,232" fill="url(#homeTone)" role="img" aria-label="Photo of the featured house for sale"/>
  </svg>

  <div class="abs brand"><span class="brand-dot"></span><span class="brand-name">Nestora</span></div>

  <h1 class="abs headline">PURCHASE<br>PRICE</h1>

  <svg class="abs" style="left:63px;top:412px" width="490" height="56" viewBox="0 0 490 56" aria-hidden="true">
    <polygon points="0,0 455,0 490,56 0,56" fill="var(--orange)"/>
  </svg>

  <!-- current mortgage -->
  <h2 class="abs col-title" style="left:63px">CURRENT MORTGAGE :</h2>
  <div class="abs row label" style="left:63px;top:553px">Loan amount :</div>
  <div class="field" style="left:299px;top:553px;width:229px">Allow input</div>
  <div class="abs row label" style="left:63px;top:593px">Interest rate&nbsp; :</div>
  <div class="field" style="left:299px;top:593px;width:229px">Allow input</div>
  <div class="abs row label" style="left:63px;top:633px">Principal &amp; Interest&nbsp; :</div>
  <div class="field" style="left:299px;top:633px;width:229px">Allow input</div>
  <div class="abs row label" style="left:63px;top:674px">Mortgage Insurance :</div>
  <div class="field" style="left:299px;top:674px;width:229px">Allow input</div>
  <div class="abs row label" style="left:63px;top:717px">Total :</div>
  <div class="field" style="left:150px;top:717px;width:378px"></div>
  <div class="abs row label" style="left:63px;top:769px">Years</div>
  <div class="field" style="left:143px;top:769px;width:68px">Input</div>
  <div class="abs row label" style="left:225px;top:769px">months</div>
  <div class="field" style="left:324px;top:769px;width:78px">Input</div>
  <div class="abs row label" style="left:410px;top:769px">left on loan</div>
  <div class="abs row label" style="left:63px;top:816px">Delta</div>
  <div class="field" style="left:150px;top:816px;width:378px">Purchase price minus loan amount</div>

  <!-- new mortgage -->
  <h2 class="abs col-title" style="left:570px">NEW MORTGAGE <span class="pct">10%</span><span class="small">DOWN<br>PAYMENT</span></h2>
  <div class="abs row label" style="left:570px;top:553px">Loan amount :</div>
  <div class="field" style="left:805px;top:553px;width:230px">70% of purchase price</div>
  <div class="abs row label" style="left:570px;top:593px">Interest rate&nbsp; :</div>
  <div class="field" style="left:805px;top:593px;width:230px">Allow input</div>
  <div class="abs row label" style="left:570px;top:633px">Principal &amp; Interest&nbsp; :</div>
  <div class="field" style="left:805px;top:633px;width:230px">Calc payment</div>
  <div class="abs row label" style="left:570px;top:674px">Mortgage Insurance :</div>
  <div class="field" style="left:805px;top:674px;width:230px">Input%</div>
  <div class="abs row label" style="left:570px;top:717px">Total :</div>
  <div class="field sm" style="left:656px;top:717px;width:379px">Interest + Montgage Principal &amp; +insusance</div>
  <div class="abs row label" style="left:570px;top:769px">Term</div>
  <div class="field sm" style="left:644px;top:769px;width:319px">Input</div>
  <div class="abs row label" style="left:987px;top:769px">year</div>
  <div class="abs row label" style="left:570px;top:818px">Down payment amount</div>
  <div class="field" style="left:845px;top:818px;width:190px"></div>

  <div class="abs diff-bar">
    <div class="diff-left">PAYMENT DIFFERENCE</div>
    <div class="diff-right">DIFFERENCE BETWEEN TOTALS</div>
  </div>

  <p class="abs tagline">THIS PROPERTY IS <em>"TAKE MY LOW RATE CERTIFIED"</em></p>

  <!-- lower band with panels -->
  <svg class="abs panels" viewBox="0 0 1100 1555" aria-hidden="false">
    <defs>
      <linearGradient id="deskTone" x1="0" y1="0" x2="1" y2="1">
        <stop offset="0" stop-color="#9aa0a8"/>
        <stop offset=".5" stop-color="#e4e4de"/>
        <stop offset="1" stop-color="#8fb3d9"/>
      </linearGradient>
    </defs>
    <polygon points="0,1078 188,1030 550,1060 912,1030 1100,1078 1100,1555 0,1555" fill="var(--mist)"/>
    <polygon points="66,1092 183,1043 301,1092 301,1462 66,1462" fill="var(--orange)"/>
    <polygon points="68,1094 183,1046 299,1094 299,1460 68,1460" fill="url(#deskTone)" role="img" aria-label="Photo of a calculator, magnifier, cash and finance charts"/>
    <polygon points="311,1092 428,1043 546,1092 546,1462 311,1462" fill="var(--orange)"/>
    <polygon points="313,1094 428,1046 544,1094 544,1460 313,1460" fill="var(--dark)"/>
    <polygon points="555,1092 672,1043 790,1092 790,1462 555,1462" fill="var(--orange)"/>
    <polygon points="801,1092 918,1043 1036,1092 1036,1462 801,1462" fill="var(--orange)"/>
    <polygon points="803,1094 918,1046 1034,1094 1034,1460 803,1460" fill="var(--dark)"/>
    <polygon points="0,1498 470,1498 505,1555 0,1555" fill="var(--ink)"/>
    <polygon points="490,1522 1100,1522 1100,1555 510,1555" fill="var(--orange)"/>
  </svg>

  <div class="abs contact" style="left:311px">
    <div class="contact-title">CONTACT INFO</div>
    <svg class="contact-icon" viewBox="0 0 54 54" aria-hidden="true">
      <circle cx="27" cy="27" r="25" fill="var(--orange)"/><circle cx="27" cy="27" r="19" fill="none" stroke="#fff" stroke-width="2"/>
      <path d="M20 18c2-1 3 0 4 2l1 3c0 1-1 2-2 2 1 3 3 5 6 6 0-1 1-2 2-2l3 1c2 1 3 2 2 4-1 2-3 3-5 2-6-2-10-6-12-12-1-2 0-5 1-6z" fill="#fff"/>
    </svg>
    <div class="contact-text">555 014 2867</div>
    <svg class="contact-icon" viewBox="0 0 54 54" aria-hidden="true">
      <circle cx="27" cy="27" r="25" fill="var(--orange)"/>
      <rect x="15" y="19" width="24" height="17" rx="2" fill="#fff"/><path d="M15 20l12 9 12-9" fill="none" stroke="var(--orange)" stroke-width="2"/>
    </svg>
    <div class="contact-text">info@nestora.com</div>
    <svg class="contact-icon" viewBox="0 0 54 54" aria-hidden="true">
      <circle cx="27" cy="27" r="25" fill="var(--orange)"/>
      <g fill="none" stroke="#fff" stroke-width="2"><circle cx="27" cy="27" r="13"/><ellipse cx="27" cy="27" rx="6" ry="13"/><path d="M14 27h26M16 20h22M16 34h22"/></g>
    </svg>
    <div class="contact-text">www.nestora.com</div>
  </div>

  <div class="abs contact alt" style="left:555px">
    <div class="contact-title">CONTACT INFO</div>
    <svg class="contact-icon" viewBox="0 0 54 54" aria-hidden="true">
      <circle cx="27" cy="27" r="25" fill="#fff"/><circle cx="27" cy="27" r="19" fill="none" stroke="var(--ink)" stroke-width="2"/>
      <path d="M20 18c2-1 3 0 4 2l1 3c0 1-1 2-2 2 1 3 3 5 6 6 0-1 1-2 2-2l3 1c2 1 3 2 2 4-1 2-3 3-5 2-6-2-10-6-12-12-1-2 0-5 1-6z" fill="var(--ink)"/>
    </svg>
    <div class="contact-text">555 014 2867</div>
    <svg class="contact-icon" viewBox="0 0 54 54" aria-hidden="true">
      <circle cx="27" cy="27" r="25" fill="#fff"/>
      <rect x="15" y="19" width="24" height="17" rx="2" fill="var(--ink)"/><path d="M15 20l12 9 12-9" fill="none" stroke="#fff" stroke-width="2"/>
    </svg>
    <div class="contact-text">info@nestora.com</div>
    <svg class="contact-icon" viewBox="0 0 54 54" aria-hidden="true">
      <circle cx="27" cy="27" r="25" fill="#fff"/>
      <g fill="none" stroke="var(--ink)" stroke-width="2"><circle cx="27" cy="27" r="13"/><ellipse cx="27" cy="27" rx="6" ry="13"/><path d="M14 27h26M16 20h22M16 34h22"/></g>
    </svg>
    <div class="contact-text">www.nestora.com</div>
  </div>

  <div class="abs panel-brand"><span class="brand-dot"></span><span class="brand-name">Nestora</span></div>

</main>
</body>
</html>
```